History Wall for Corporate Office

We are working on our corporate office wall to include a graphic with our history, and when we opened the schools and dance studios.
We are looking for a professional look, vibrant graphic, but clean and very clear to understand.
The wall is going up from floor 1 to floor 2. Please see photos attached as reference.
Measurements provided as well.
Do not include the master logo as part of this design, as the master logo it's placed in the wall right next to this one (photo as reference will show this).
Things to consider:
- We want to include photos of the schools/studio openings. Attached are the photos of each school opening.
- Follow brand guidelines
- Mainly using Master Color palette (blues and yellows) with touches of the other colors if needed
Here's the order of school/studio openings:
1968 Bright Path Hollowmere
1971 Bright Path Fernwick
1975 Bright Path Harlow
1976 The Bright Path Conservatory of Dance
1978 Bright Path Collegiate
1979 Bright Path Cobalt • Preschool & Elementary School
1980 Bright Path Las Brisas
1981 Bright Path Cedar Crest
1984 Bright Path Middle School
1989 Bright Path Dorsey
1990 Bright Path Whitford
2005 Bright Path Garnet
2008 Bright Path Schools 40th Anniversary
2015 NHMS Talbot Studio
2016 NHMS Aspen Hollow Studio
2017 NHMS Cedar Crest Studio
2018 Bright Path Schools 50th Anniversary
2021 Kinetic Leagues Coastline
2022 NHMS Cedar Crest Studio
2024 Bright Path Sutter Ridge
Fonts to be used: Fellix (main font) and Handsome (highlights-if needed)
Sending two graphic ideas as reference of the design direction we would like to have.

```html
<!DOCTYPE html>
<html lang="en">
<head>
<meta charset="utf-8">
<title>Bright Path — History Wall</title>
<link rel="stylesheet" href="https://fonts.googleapis.com/css2?family=Figtree:wght@400;800&display=swap">
<style>
  :root{
    --navy:#0e1a5c;
    --yellow:#f4b63f;
    --green:#4caf75;
    --purple:#3a2484;
    --blue:#4a8be6;
    --steel:#2e6db5;
    --red:#8b1c1c;
    --crimson:#d0312d;
    --forest:#2d6b50;
    --orange:#ef7636;
    --step1:#e0f2f9;
    --step2:#d0dfe6;
    --step3:#a5bfcc;
    --step4:#75a2b6;
    --step5:#467f99;
    --step6:#1a5e80;
    --step7:#134a68;
    --step8:#0d3149;
    --paper:#ffffff;
  }
  *{margin:0;padding:0;box-sizing:border-box}
  html,body{width:1200px;height:818px;overflow:hidden;background:var(--paper)}
  .wall{
    position:relative;width:2324px;height:1583px;
    transform:scale(0.51635);transform-origin:0 0;
    font-family:"Figtree",sans-serif;
  }
  .wall-graphics{position:absolute;inset:0;width:2324px;height:1583px}
  .milestone{position:absolute;width:120px;display:flex;flex-direction:column}
  .milestone--wide{width:138px}
  .milestone .frame{
    flex-shrink:0;
    background:var(--paper);border:3px solid var(--c);
    padding:11px 11px 10px;height:var(--ph);
  }
  .milestone .photo{
    width:100%;height:100%;
    background:linear-gradient(160deg,var(--c) 0%,#f2e9d8 45%,var(--c) 100%);
    opacity:.85;
  }
  .milestone .caption{
    flex-shrink:0;
    background:var(--c);color:#fff;min-height:var(--ch);
    padding:10px 4px 8px 13px;
    font-size:16px;line-height:15.5px;
    overflow-wrap:normal;
  }
  .caption .year{display:block;font-weight:800;font-size:28px;line-height:25px;margin-bottom:1px;letter-spacing:-.5px}
  .caption .note{display:block;margin-top:10px}
  .caption sup{font-size:9px;line-height:0}
  .caption--dark{color:var(--navy)}
  .year--accent{color:var(--yellow)}
</style>
</head>
<body>
<main class="wall" aria-label="Bright Path history timeline">
  <svg class="wall-graphics" viewBox="0 0 2324 1583" aria-hidden="true">
    <g class="staircase">
      <rect x="297" y="1488" width="206" height="95" fill="var(--step1)"/>
      <rect x="503" y="1428" width="216" height="155" fill="var(--step2)"/>
      <rect x="719" y="1320" width="209" height="263" fill="var(--step3)"/>
      <rect x="928" y="1218" width="214" height="365" fill="var(--step4)"/>
      <rect x="1142" y="1117" width="200" height="466" fill="var(--step5)"/>
      <rect x="1342" y="1024" width="273" height="559" fill="var(--step6)"/>
      <rect x="1615" y="929" width="293" height="654" fill="var(--step7)"/>
      <rect x="1908" y="823" width="416" height="760" fill="var(--step8)"/>
    </g>
    <g class="connectors" fill="none" stroke-width="5">
      <polyline points="161,1127 161,996 203,996" stroke="var(--navy)"/>
      <polyline points="275,1127 275,1236 321,1236" stroke="var(--yellow)"/>
      <polyline points="371,1106 371,981 412,981" stroke="var(--green)"/>
      <polyline points="475,885 475,825 540,825" stroke="var(--purple)"/>
      <polyline points="582,993 582,1086 622,1086" stroke="var(--blue)"/>
      <polyline points="739,1163 789,1163 789,993" stroke="var(--crimson)"/>
      <polyline points="764,781 764,718 822,718" stroke="var(--yellow)"/>
      <polyline points="873,858 873,946 922,946" stroke="var(--forest)"/>
      <polyline points="1039,1010 1095,1010 1095,858" stroke="var(--purple)"/>
      <polyline points="1085,646 1085,586 1141,586" stroke="var(--navy)"/>
      <polyline points="1181,718 1181,806 1222,806" stroke="var(--red)"/>
      <polyline points="1339,885 1390,885 1390,718" stroke="var(--blue)"/>
      <polyline points="1382,507 1382,436 1441,436" stroke="var(--forest)"/>
      <polyline points="1482,580 1482,667 1522,667" stroke="var(--orange)"/>
      <polyline points="1639,735 1697,735 1697,582" stroke="var(--steel)"/>
      <polyline points="1679,370 1679,313 1741,313" stroke="var(--green)"/>
      <polyline points="1782,438 1782,548 1822,548" stroke="var(--crimson)"/>
      <polyline points="1939,580 1990,580 1990,440" stroke="var(--blue)"/>
      <polyline points="1982,229 1982,157 2041,157" stroke="var(--yellow)"/>
      <polyline points="2158,157 2198,157" stroke="var(--green)"/>
    </g>
    <polygon class="timeline-arrow" points="2195,133 2219,157 2195,181" fill="var(--green)"/>
  </svg>

  <article class="milestone milestone--wide" style="--c:var(--navy);--ph:138px;--ch:86px;left:101px;top:1127px">
    <div class="caption"><span class="year year--accent">1968</span>Bright Path Hollowmere</div>
    <div class="frame"><div class="photo" role="img" aria-label="Photo of the Bright Path Hollowmere opening"></div></div>
  </article>

  <article class="milestone" style="--c:var(--yellow);--ph:118px;--ch:81px;left:201px;top:928px">
    <div class="frame"><div class="photo" role="img" aria-label="Photo of the Bright Path Fernwick opening"></div></div>
    <div class="caption caption--dark"><span class="year">1971</span>Bright Path Fernwick</div>
  </article>

  <article class="milestone" style="--c:var(--green);--ph:124px;--ch:88px;left:319px;top:1106px">
    <div class="frame"><div class="photo" role="img" aria-label="Photo of the Bright Path Harlow opening"></div></div>
    <div class="caption"><span class="year">1975</span>Bright Path Harlow</div>
  </article>

  <article class="milestone" style="--c:var(--purple);--ph:115px;--ch:105px;left:410px;top:885px;width:129px">
    <div class="frame"><div class="photo" role="img" aria-label="Photo of the Bright Path Conservatory of Dance opening"></div></div>
    <div class="caption"><span class="year">1976</span>The Bright Path Conservatory of Dance</div>
  </article>

  <article class="milestone" style="--c:var(--blue);--ph:116px;--ch:96px;left:538px;top:781px">
    <div class="frame"><div class="photo" role="img" aria-label="Photo of the Bright Path Collegiate opening"></div></div>
    <div class="caption"><span class="year">1978</span>Bright Path Collegiate</div>
  </article>

  <article class="milestone" style="--c:var(--red);--ph:117px;--ch:137px;left:620px;top:993px">
    <div class="frame"><div class="photo" role="img" aria-label="Photo of the Bright Path Cobalt opening"></div></div>
    <div class="caption"><span class="year">1979</span>Bright Path Cobalt<span class="note">Preschool &amp; Elementary School</span></div>
  </article>

  <article class="milestone" style="--c:var(--yellow);--ph:116px;--ch:96px;left:702px;top:781px">
    <div class="frame"><div class="photo" role="img" aria-label="Photo of the Bright Path Las Brisas opening"></div></div>
    <div class="caption caption--dark"><span class="year">1980</span>Bright Path Las Brisas</div>
  </article>

  <article class="milestone" style="--c:var(--forest);--ph:114px;--ch:98px;left:820px;top:646px">
    <div class="frame"><div class="photo" role="img" aria-label="Photo of the Bright Path Cedar Crest opening"></div></div>
    <div class="caption"><span class="year">1981</span>Bright Path Cedar Crest</div>
  </article>

  <article class="milestone" style="--c:var(--purple);--ph:119px;--ch:94px;left:920px;top:858px">
    <div class="frame"><div class="photo" role="img" aria-label="Photo of the Bright Path Middle School opening"></div></div>
    <div class="caption"><span class="year">1984</span>Bright Path Middle School</div>
  </article>

  <article class="milestone" style="--c:var(--navy);--ph:124px;--ch:88px;left:1020px;top:646px">
    <div class="frame"><div class="photo" role="img" aria-label="Photo of the Bright Path Dorsey opening"></div></div>
    <div class="caption"><span class="year">1989</span>Bright Path Dorsey</div>
  </article>

  <article class="milestone" style="--c:var(--red);--ph:120px;--ch:91px;left:1139px;top:507px">
    <div class="frame"><div class="photo" role="img" aria-label="Photo of the Bright Path Whitford opening"></div></div>
    <div class="caption"><span class="year">1990</span>Bright Path Whitford</div>
  </article>

  <article class="milestone" style="--c:var(--blue);--ph:124px;--ch:89px;left:1220px;top:718px">
    <div class="frame"><div class="photo" role="img" aria-label="Photo of the Bright Path Garnet opening"></div></div>
    <div class="caption"><span class="year">2005</span>Bright Path Garnet</div>
  </article>

  <article class="milestone" style="--c:var(--forest);--ph:120px;--ch:91px;left:1320px;top:507px">
    <div class="frame"><div class="photo" role="img" aria-label="Photo from the Bright Path Schools 40th anniversary"></div></div>
    <div class="caption"><span class="year">2008</span>Bright Path Schools 40<sup>th</sup> Anniversary</div>
  </article>

  <article class="milestone" style="--c:var(--orange);--ph:118px;--ch:92px;left:1439px;top:370px">
    <div class="frame"><div class="photo" role="img" aria-label="Photo of the NHMS Talbot Studio opening"></div></div>
    <div class="caption"><span class="year">2015</span>NHMS Talbot Studio</div>
  </article>

  <article class="milestone" style="--c:var(--steel);--ph:118px;--ch:95px;left:1520px;top:582px">
    <div class="frame"><div class="photo" role="img" aria-label="Photo of the NHMS Aspen Hollow Studio opening"></div></div>
    <div class="caption"><span class="year">2016</span>NHMS Aspen Hollow Studio</div>
  </article>

  <article class="milestone" style="--c:var(--green);--ph:118px;--ch:94px;left:1620px;top:370px">
    <div class="frame"><div class="photo" role="img" aria-label="Photo of the NHMS Cedar Crest Studio opening"></div></div>
    <div class="caption"><span class="year">2017</span>NHMS Cedar Crest Studio</div>
  </article>

  <article class="milestone" style="--c:var(--red);--ph:121px;--ch:88px;left:1739px;top:229px">
    <div class="frame"><div class="photo" role="img" aria-label="Photo from the Bright Path Schools 50th anniversary"></div></div>
    <div class="caption"><span class="year">2018</span>Bright Path Schools 50<sup>th</sup> Anniversary</div>
  </article>

  <article class="milestone" style="--c:var(--blue);--ph:119px;--ch:93px;left:1820px;top:441px">
    <div class="frame"><div class="photo" role="img" aria-label="Photo of the Kinetic Leagues Coastline opening"></div></div>
    <div class="caption"><span class="year">2021</span>Kinetic Leagues Coastline</div>
  </article>

  <article class="milestone" style="--c:var(--yellow);--ph:116px;--ch:95px;left:1920px;top:229px">
    <div class="frame"><div class="photo" role="img" aria-label="Photo of the NHMS Cedar Crest Studio opening"></div></div>
    <div class="caption"><span class="year">2022</span>NHMS Cedar Crest Studio</div>
  </article>

  <article class="milestone" style="--c:var(--green);--ph:117px;--ch:95px;left:2039px;top:88px">
    <div class="frame"><div class="photo" role="img" aria-label="Photo of the Bright Path Sutter Ridge opening"></div></div>
    <div class="caption"><span class="year">2024</span>Bright Path Sutter Ridge</div>
  </article>
</main>
</body>
</html>
```